Redesign PixelHarbor's Designer Account Home Page

Are a web designer? New to PixelHarbor? This contest is for you!

We want you to redesign PixelHarbor's designer account home page. We're looking for bold and innovative ideas to make this page a useful and fun experience for you and your fellow designers.

Only new registrants this month are eligible to enter this contest and win prizes.

Your task:
* We want you to put your web design skills to the test and re-design the My Account home page ("Overview") on PixelHarbor to make it more functional and engaging for designers on PixelHarbor.
* The page you are redesigning is here: http://www.pixelharbor-example.com/my-profile.
* Your design should allow for the same functionality as the existing page, though you don't need to replicate the same elements (buttons) or the same menu structure.
* Your design must fit with the branding of the site.
* You must provide a brief outline of what changes you made and why when you upload your design
* 1 submission per designer - make it your best work!
* Pls see "Must haves" for requirements.

Deadline:
* Submit before 12:00am 1st September UTC. Pls convert this deadline to your local timezone and take note of the local time and date

Prizes: $1,000 to win
* First prize for the best design is $700
* Second prize is $200
* Third prize is $100

If you started from scratch, how would you design the MyAccount page on PixelHarbor?

Good luck & have fun!

Mel / The PixelHarbor Team

Target Market(s)

PixelHarbor designers

Number of Pages Required

1 page

Requirements
Must have
• Dimensions: 1200 x 1000 px
• Minimum 150-300 dpi
• Your design must adhere to our quality standards to be eligible to receive a prize
• Submissions must be created in Adobe Creative Suite (Illustrator or Photoshop)
• Your design must fit with the branding of the PixelHarbor site.
• Only new registrants this month are eligible to enter and win prizes.

```html
<!DOCTYPE html>
<html lang="en">
<head>
<meta charset="utf-8">
<title>PixelHarbor – Overview</title>
<link rel="stylesheet" href="https://fonts.googleapis.com/css2?family=Open+Sans:wght@400;600;700&display=swap">
<style>
:root{
  --bg:#eeeff1;
  --panel:#ffffff;
  --line:#dcdee2;
  --dark:#2c2e31;
  --darker:#232427;
  --text:#3a3d42;
  --muted:#8a8f96;
  --blue:#1f8dc6;
  --blue-dark:#176f9e;
  --green:#7dbb3c;
  --green-dark:#67a02c;
  --footer-text:#a9adb3;
}
*{box-sizing:border-box;margin:0;padding:0}
html,body{width:805px;height:1200px;overflow:hidden}
body{background:var(--bg);font-family:"Open Sans",Arial,sans-serif;color:var(--text);position:relative;font-size:11px}
.abs{position:absolute}

/* header */
.site-header{left:0;top:0;width:805px;height:46px;background:var(--dark);display:flex;align-items:center;padding:0 16px}
.brand{display:flex;align-items:center;gap:6px;color:#fff;font-weight:700;font-size:16px}
.brand-mark{width:14px;height:14px;background:var(--green)}
.main-nav{display:flex;gap:14px;margin-left:22px;color:#d7dadd;font-size:10px}
.flag{width:16px;height:10px;background:#2a4d9b;align-self:center}
.header-right{margin-left:auto;display:flex;gap:8px;align-items:center}
.profile-menu{background:#fff;color:var(--text);font-size:10px;padding:4px 18px 4px 8px;border-radius:2px}
.submit-btn{background:var(--green);color:#fff;font-size:10px;font-weight:600;padding:5px 12px;border-radius:2px}
.breadcrumb{left:0;top:46px;width:805px;height:22px;background:#e3e5e8;border-bottom:1px solid var(--line);padding:0 16px;display:flex;align-items:center;gap:6px;font-size:9.5px;color:var(--muted)}
.page-title{left:0;top:78px;width:805px;text-align:center;font-size:25px;font-weight:600;color:var(--text)}

/* sidebar */
.sidebar{left:66px;top:132px;width:222px}
.browse-btn{display:block;background:var(--green);color:#fff;font-weight:700;font-size:14px;padding:8px 14px;border-bottom:3px solid var(--green-dark)}
.side-menu{list-style:none;margin-top:8px;background:var(--panel);border:1px solid var(--line)}
.side-menu li{height:30px;display:flex;align-items:center;padding:0 12px;border-bottom:1px solid var(--line);font-size:10px;color:#6d7278;gap:8px}
.side-menu li::before{content:"";width:8px;height:8px;background:#c4c8cd;border-radius:1px}
.side-menu li.active{background:var(--blue);color:#fff}
.side-menu li.active::before{background:#fff}

/* panels */
.panel{background:var(--panel);border:1px solid var(--line)}
.profile-card{left:320px;top:132px;width:462px;height:156px;display:flex;align-items:center;padding:0 18px}
.avatar{width:54px;height:54px;background:#c9ced4}
.stats{display:flex;margin-left:30px;flex:1}
.stat{flex:1;text-align:center}
.stat-label{font-size:10px;color:var(--muted)}
.stat-value{font-size:17px;color:#a3a8ae;margin:4px 0}
.stat-value.positive{color:var(--blue)}
.stat-note{font-size:8px;color:#b2b6bb}

.setup-panel{left:320px;top:300px;width:462px;height:544px;padding:16px 18px}
.panel-heading{font-size:17px;font-weight:600;color:var(--text)}
.progress{margin-top:16px;height:40px;background:var(--blue);border:1px solid var(--blue-dark);display:flex;align-items:center;padding:0 8px}
.progress-pct{background:var(--green);color:#fff;font-weight:700;font-size:14px;padding:5px 8px}
.progress-track{flex:1;height:12px;margin-left:8px;background:#e8ecef;position:relative}
.progress-track span{position:absolute;left:0;top:0;bottom:0;width:57%;background:#fff}
.subheading{font-size:17px;font-weight:600;margin-top:24px}
.todo-grid{margin-top:10px;border:1px solid var(--line);padding:8px;display:grid;grid-template-columns:1fr 1fr;gap:8px}
.todo{height:30px;background:#f3f4f6;border:1px solid #e3e5e8;display:flex;align-items:center;gap:6px;padding:0 8px;font-size:9px;color:#666b72}
.todo::before{content:"";width:10px;height:10px;border-radius:50%;background:var(--green);flex:none}
.todo.highlight{background:var(--blue);color:#fff;border-color:var(--blue-dark);font-weight:600}
.todo.highlight::before{background:#fff}
.jobs-box{margin-top:10px;border:1px solid var(--line);padding:10px}
.jobs-intro{font-size:9px;color:var(--muted);text-align:center}
.job-list{display:grid;grid-template-columns:1fr 1fr;gap:10px;margin-top:8px}
.job{border-top:1px solid var(--line);padding-top:6px}
.job-title{font-size:9px;color:var(--blue);font-weight:600}
.job-meta{display:grid;grid-template-columns:1fr 1fr;gap:4px;margin-top:6px;font-size:8.5px;color:var(--muted)}
.pager{margin-top:12px;text-align:center;font-size:9px;color:var(--muted);letter-spacing:3px}
.pager b{color:var(--blue)}

.achievements{left:320px;top:856px;width:462px;height:172px;padding:16px 18px}
.ach-intro{font-size:9px;color:var(--muted);margin-top:6px}
.ach-list{display:grid;grid-template-columns:1fr 1fr;gap:14px;margin-top:12px}
.ach{display:flex;gap:8px;align-items:center}
.ach-icon{width:32px;height:32px;border-radius:50%;background:var(--blue);flex:none}
.ach-name{font-size:10px;font-weight:700;color:var(--blue)}
.ach-desc{font-size:8.5px;color:var(--muted)}

/* footer */
.site-footer{left:0;top:1044px;width:805px;height:134px;background:var(--dark);display:flex;padding:14px 40px 0;gap:22px;color:var(--footer-text)}
.f-col h4{color:#fff;font-size:11px;font-weight:600;margin-bottom:6px}
.f-col li{list-style:none;font-size:7.5px;line-height:13px}
.f-col.narrow{width:100px}
.tags{display:flex;flex-wrap:wrap;gap:3px;width:130px}
.tags span{border:1px solid #4a4d52;font-size:7px;padding:1px 4px}
.subscribe{margin-left:auto;width:160px}
.sub-row{display:flex}
.sub-row div{flex:1;height:16px;background:#fff}
.sub-row span{background:var(--green);color:#fff;font-size:8px;padding:2px 6px}
.socials{display:flex;gap:6px;margin-top:10px}
.socials i{width:16px;height:16px;border-radius:50%;background:#5b5f65}
.flags{display:flex;gap:5px;margin-top:10px}
.flags i{width:16px;height:10px;background:#7b7f86}
.copyright{left:0;top:1178px;width:805px;height:22px;background:var(--darker);color:#7d8187;font-size:7.5px;display:flex;align-items:center;justify-content:center}
</style>
</head>
<body>

<header class="abs site-header">
  <div class="brand"><span class="brand-mark"></span>PixelHarbor</div>
  <nav class="main-nav"><span>Categories</span><span>Designers</span><span>Browse Jobs</span><span>How it works</span><span class="flag" role="img" aria-label="Country flag"></span></nav>
  <div class="header-right"><span class="profile-menu">My Profile ▾</span><span class="submit-btn">Submit work</span></div>
</header>
<div class="abs breadcrumb">
  <svg width="10" height="9" viewBox="0 0 10 9"><path d="M5 0L0 4h1.5v5h2.5V6h2v3h2.5V4H10z" fill="#8a8f96"/></svg>
  <span>Home</span><span>›</span><span>My Profile</span>
</div>
<h1 class="abs page-title">Overview</h1>

<aside class="abs sidebar">
  <span class="browse-btn">Browse Jobs</span>
  <ul class="side-menu">
    <li class="active">Overview</li>
    <li>Dashboard</li>
    <li>Invites</li>
    <li>Questions</li>
    <li>Messages</li>
    <li>Settings</li>
    <li>Rewards</li>
    <li>Projects</li>
    <li>My Profile</li>
  </ul>
</aside>

<section class="abs panel profile-card">
  <div class="avatar" role="img" aria-label="Designer profile photo"></div>
  <div class="stats">
    <div class="stat"><div class="stat-label">Rank</div><div class="stat-value">#435699</div><div class="stat-note">out of 742,000 users</div></div>
    <div class="stat"><div class="stat-label">Positive</div><div class="stat-value positive">0%</div><div class="stat-note">rating</div></div>
    <div class="stat"><div class="stat-label">Submissions</div><div class="stat-value">0</div><div class="stat-note">this month</div></div>
    <div class="stat"><div class="stat-label">Earnings</div><div class="stat-value">$0.00</div><div class="stat-note">earned this month</div></div>
  </div>
</section>

<section class="abs panel setup-panel">
  <h2 class="panel-heading">Getting Started-Complete Your Profile</h2>
  <div class="progress"><span class="progress-pct">57 %</span><div class="progress-track"><span></span></div></div>
  <h3 class="subheading">Things left to do:</h3>
  <div class="todo-grid">
    <div class="todo">Tell us what type of designer you are</div>
    <div class="todo">Add an about me to your profile</div>
    <div class="todo highlight">Verify your payment address</div>
    <div class="todo">Review &amp; accept the designer agreement</div>
    <div class="todo">Visit the Jobs Board</div>
    <div class="todo">Submit your first designs</div>
    <div class="todo">Add your profile pic</div>
  </div>
  <h3 class="subheading">Recommended Jobs</h3>
  <div class="jobs-box">
    <p class="jobs-intro">There is over 10865 jobs waiting for you on these jobs that don't have any submissions yet.</p>
    <div class="job-list">
      <div class="job"><div class="job-title">Modern, funky architectural property developer...</div>
        <div class="job-meta"><span>10 days left</span><span>0 entries</span><span>$250 prize</span><span>Logo design</span></div></div>
      <div class="job"><div class="job-title">Modern, funky architectural property developer...</div>
        <div class="job-meta"><span>10 days left</span><span>0 entries</span><span>$250 prize</span><span>Logo design</span></div></div>
    </div>
    <div class="pager">‹ prev 1 <b>2</b> 3 4 5 next ›</div>
  </div>
</section>

<section class="abs panel achievements">
  <h2 class="panel-heading">Achievements</h2>
  <p class="ach-intro">Earn designer level achievements as you hit milestones.</p>
  <div class="ach-list">
    <div class="ach"><span class="ach-icon"></span><div><div class="ach-name">Rookie (Next)</div><div class="ach-desc">Submit at least 1 design to contests</div></div></div>
    <div class="ach"><span class="ach-icon"></span><div><div class="ach-name">Top 15000 Designer (Next)</div><div class="ach-desc">Submit at least 1 design to contests</div></div></div>
  </div>
</section>

<footer class="abs site-footer">
  <div class="f-col narrow"><h4>I need a...</h4><ul><li>Logo design</li><li>Website design</li><li>Business card</li><li>Flyer design</li><li>Banner design</li><li>Brochure design</li></ul></div>
  <div class="f-col narrow"><h4>Find a...</h4><ul><li>Logo designer</li><li>Web designer</li><li>Graphic designer</li><li>Print designer</li><li>Freelancer</li><li>Illustrator</li></ul></div>
  <div class="f-col narrow"><h4>About us</h4><ul><li>Our story</li><li>How it works</li><li>Press</li><li>Careers</li><li>Contact us</li><li>Help centre</li></ul></div>
  <div class="f-col"><h4>Popular pages</h4><div class="tags"><span>Logo ideas</span><span>Web design</span><span>Business cards</span><span>Flyers</span><span>Banners</span><span>T-shirts</span><span>Packaging</span><span>Icons</span></div></div>
  <div class="f-col subscribe"><h4>Subscribe to our newsletter</h4>
    <div class="sub-row"><div></div><span>Go</span></div>
    <div class="socials"><i role="img" aria-label="Social link"></i><i role="img" aria-label="Social link"></i><i role="img" aria-label="Social link"></i><i role="img" aria-label="Social link"></i></div>
    <div class="flags"><i role="img" aria-label="Region flag"></i><i role="img" aria-label="Region flag"></i><i role="img" aria-label="Region flag"></i><i role="img" aria-label="Region flag"></i><i role="img" aria-label="Region flag"></i></div>
  </div>
</footer>
<div class="abs copyright">© PixelHarbor. All rights reserved. Terms of use · Privacy policy</div>

</body>
</html>
```